Bref créative
Brightfield pest control
Stationary business card project for brightfield pest control
Professional
Doug Harlan
4120 w pinecrest ln. meridian idaho 83619
dharlan77@mailvista.net
ALL SERVICES GUARANTEED
Residential.Commercial Service.Certified specialist.Free Estimates
This is the company logo.

```html
<!DOCTYPE html>
<html lang="en">
<head>
<meta charset="utf-8">
<title>Brightfield pest control – Business card</title>
<link rel="stylesheet" href="https://fonts.googleapis.com/css2?family=PT+Sans:wght@400;700&display=swap">
<style>
  :root {
    --page: #ffffff;
    --sky-top: #a9d3e1;
    --sky-bottom: #dcf0f6;
    --band-light: #fdf5dc;
    --band-warm: #f6d6a2;
    --logo-panel: #fdf6d6;
    --brand-orange: #f47b20;
    --brand-green: #4fd11a;
    --navy: #0e1f5c;
    --name-navy: #1a2a6c;
    --white: #ffffff;
  }
  * { margin: 0; padding: 0; box-sizing: border-box; }
  html, body {
    width: 1200px;
    height: 744px;
    overflow: hidden;
    background: var(--page);
    font-family: "PT Sans", sans-serif;
  }
  .canvas {
    position: relative;
    width: 1200px;
    height: 744px;
  }
  .business-card {
    position: absolute;
    left: 34px;
    top: 65px;
    width: 1133px;
    height: 614px;
    border-top-right-radius: 96px;
    overflow: hidden;
    background: linear-gradient(180deg, var(--sky-top) 0%, var(--sky-bottom) 100%);
  }
  .accent-band {
    position: absolute;
    left: 120px;
    right: 0;
    top: 120px;
    height: 134px;
    background: linear-gradient(90deg, var(--band-light) 0%, var(--band-light) 40%, var(--band-warm) 100%);
  }
  .logo-panel {
    position: absolute;
    left: 120px;
    top: 43px;
    width: 432px;
    height: 418px;
    background: var(--logo-panel);
    display: flex;
    flex-direction: column;
    align-items: center;
    justify-content: center;
    gap: 26px;
  }
  .logo-dot {
    width: 110px;
    height: 110px;
    border-radius: 50%;
    background: var(--brand-green);
  }
  .logo-name {
    color: var(--brand-orange);
    font-weight: 700;
    font-size: 64px;
    line-height: 1;
    text-align: center;
    letter-spacing: -1px;
  }
  .contact-name {
    position: absolute;
    right: 72px;
    top: 188px;
    color: var(--name-navy);
    font-size: 44px;
    font-weight: 400;
    line-height: 1;
  }
  .contact-bar {
    position: absolute;
    left: 0;
    right: 0;
    bottom: 0;
    height: 100px;
    background: var(--navy);
    color: var(--white);
    font-size: 29px;
    line-height: 36px;
    text-align: center;
    padding-top: 12px;
  }
  .contact-bar .divider {
    display: inline-block;
    width: 3px;
    height: 28px;
    background: var(--white);
    margin: 0 6px;
    vertical-align: -5px;
  }
</style>
</head>
<body>
  <main class="canvas">
    <section class="business-card" aria-label="Brightfield pest control business card">
      <div class="accent-band"></div>
      <div class="logo-panel">
        <span class="logo-dot" aria-hidden="true"></span>
        <p class="logo-name">brightfield<br>pest control</p>
      </div>
      <p class="contact-name">Doug Harlan</p>
      <div class="contact-bar">
        <p>Cell (208)555-0143<span class="divider"></span>4120 w pinecrest ln. meridian idaho 83619</p>
        <p>Email dharlan77@mailvista.net</p>
      </div>
    </section>
  </main>
</body>
</html>
```